Business Card for premium dental clinic

We are a premium dental clinic based in Brasov, Romania with more than 15 year on the market, providing quality dental treatment made by a team of more specialized dentists, working with modern equipment as a solution to beautiful and healthy teeth.

Our current logo for the clinic use 2 square with colors black and gold - dr Corbescu - studio, using family fonts Bodoni, Myriad Pro and Segoe Print.
Depending on the printing we used some gold CMYK background or gold foil picture background or a gold gradient.
We want a business card:
- eye catching business card
- distinguished business card
- premium design
- to keep the color scheme of black and gold
- to attract the customers to spent time reading the information
- modern concept

```html
<!DOCTYPE html>
<html lang="en">
<head>
<meta charset="utf-8">
<title>dr Corbescu studio – business card</title>
<link rel="stylesheet" href="https://fonts.googleapis.com/css2?family=Lato:wght@400;700;900&family=Roboto+Condensed:wght@400&display=swap">
<style>
  :root {
    --ink: #050708;
    --paper: #ffffff;
    --gold: #f2c12e;
    --gold-deep: #d9a21b;
    --gold-light: #ffe27a;
    --copper: #d38a2a;
    --muted: #3f4347;
    --backdrop: #e9e6e1;
  }
  * { margin: 0; padding: 0; box-sizing: border-box; }
  html, body {
    width: 1200px;
    height: 1023px;
    overflow: hidden;
    background: var(--backdrop);
    font-family: "Lato", sans-serif;
  }
  .canvas { position: relative; width: 1200px; height: 1023px; }

  .card {
    position: absolute;
    left: 248px;
    width: 681px;
    height: 390px;
    overflow: hidden;
    box-shadow: 0 6px 16px rgba(0,0,0,0.25);
  }
  .card--front { top: 87px; background: var(--paper); }
  .card--back { top: 541px; background: var(--ink); }

  /* front */
  .front-wave { position: absolute; inset: 0; }
  .brand {
    position: absolute;
    font-family: "Lato", sans-serif;
    font-weight: 400;
    color: var(--ink);
    line-height: 1.05;
  }
  .card--front .brand { left: 44px; top: 86px; font-size: 50px; }

  .person { position: absolute; right: 27px; top: 36px; text-align: right; }
  .person__name {
    font-weight: 900;
    font-size: 35px;
    color: var(--copper);
    letter-spacing: 0.5px;
  }
  .person__role { font-size: 17px; color: var(--muted); margin-top: 2px; }

  .contact {
    position: absolute;
    right: 27px;
    top: 215px;
    text-align: right;
    color: var(--paper);
    font-size: 18.5px;
  }
  .contact__address { line-height: 24px; margin-bottom: 14px; }
  .contact__row {
    display: flex;
    justify-content: flex-end;
    align-items: center;
    gap: 10px;
    height: 31px;
  }
  .contact__icon { width: 18px; height: 18px; flex: none; }

  /* back */
  .foil {
    position: absolute;
    left: 0; top: 0;
    width: 342px; height: 390px;
    background: radial-gradient(circle at 40% 35%, var(--gold-light), var(--gold) 45%, var(--gold-deep) 100%);
  }
  .brand-plate {
    position: absolute;
    left: 38px; top: 123px;
    width: 304px; height: 143px;
    background: var(--paper);
    display: flex;
    align-items: center;
    justify-content: center;
  }
  .brand-plate .brand { position: static; font-size: 38px; text-align: center; }
  .tagline {
    position: absolute;
    right: 12px;
    bottom: 16px;
    font-family: "Roboto Condensed", sans-serif;
    font-size: 46px;
    color: var(--paper);
  }
</style>
</head>
<body>
<main class="canvas">

  <section class="card card--front" aria-label="Business card front">
    <svg class="front-wave" width="681" height="390" viewBox="0 0 681 390" aria-hidden="true">
      <path d="M0,285 C60,315 100,325 160,320 C300,305 400,186 560,186 C620,186 660,200 681,216 L681,390 L0,390 Z" fill="var(--ink)"/>
    </svg>

    <p class="brand">dr Corbescu<br>studio</p>

    <div class="person">
      <h1 class="person__name">JOHN SMITH</h1>
      <p class="person__role">Managing Director</p>
    </div>

    <address class="contact" style="font-style:normal">
      <p class="contact__address">2345 First Address Line<br>Second Address Line, 56324</p>
      <p class="contact__row">123 456 7890
        <svg class="contact__icon" viewBox="0 0 24 24" aria-hidden="true"><path d="M6.6 10.8a15.1 15.1 0 0 0 6.6 6.6l2.2-2.2a1 1 0 0 1 1-.25 11.4 11.4 0 0 0 3.6.57 1 1 0 0 1 1 1V20a1 1 0 0 1-1 1A17 17 0 0 1 3 4a1 1 0 0 1 1-1h3.5a1 1 0 0 1 1 1c0 1.25.2 2.45.57 3.57a1 1 0 0 1-.25 1z" fill="var(--paper)"/></svg>
      </p>
      <p class="contact__row">lorem@yourwebsite.com
        <svg class="contact__icon" viewBox="0 0 24 24" aria-hidden="true"><rect x="2" y="5" width="20" height="14" fill="var(--paper)"/><path d="M2 5l10 8 10-8M2 19l7-7M22 19l-7-7" stroke="var(--ink)" stroke-width="1.5" fill="none"/></svg>
      </p>
      <p class="contact__row">www.yourwebsite.com
        <svg class="contact__icon" viewBox="0 0 24 24" aria-hidden="true"><g fill="none" stroke="var(--paper)" stroke-width="1.6"><circle cx="12" cy="12" r="10"/><ellipse cx="12" cy="12" rx="4.5" ry="10"/><path d="M2 12h20M4 7h16M4 17h16"/></g></svg>
      </p>
    </address>
  </section>

  <section class="card card--back" aria-label="Business card back">
    <div class="foil" role="img" aria-label="Crumpled gold foil texture"></div>
    <div class="brand-plate">
      <p class="brand">dr Corbescu<br>studio</p>
    </div>
    <p class="tagline">dental clinic</p>
  </section>

</main>
</body>
</html>
```